Stationery Design Project

We are looking stationary Design for Velbrin Global, a high end clothing company. I have attached an image of our Logo below.
Updates
I am looking for designs for the following stationaries:
1. Leather Binders
2. Paper Binders
3. Letterhead
4. Envelopes
5. Pens, pencils etc
We would love to see designs with gold, black and white color combination.
Industry/Entity Type
Clothing
Look and feel
Each slider illustrates characteristics of the customer's brand and the style your logo design should communicate.

```html
<!DOCTYPE html>
<html lang="en">
<head>
<meta charset="utf-8">
<title>Velbrin Global Letterhead</title>
<link href="https://fonts.googleapis.com/css2?family=Playfair+Display:wght@700&display=swap" rel="stylesheet">
<style>
  :root {
    --ink: #0a0a0a;
    --band: #0c0c0b;
    --damask-light: #45423a;
    --damask-mid: #34322d;
    --damask-dark: #262521;
    --cream: #fdfbea;
    --cream-shade: #f7f4df;
  }
  html, body {
    margin: 0;
    padding: 0;
    overflow: hidden;
    background: var(--cream);
  }
  .letterhead {
    position: relative;
    width: 848px;
    height: 1200px;
    overflow: hidden;
    background: var(--cream);
  }
  .paper-pattern {
    position: absolute;
    inset: 0;
    background: linear-gradient(180deg, var(--cream) 0%, var(--cream) 40%, var(--cream-shade) 100%);
  }
  .header-damask {
    position: absolute;
    left: 0;
    top: 0;
    width: 848px;
    height: 195px;
    background:
      radial-gradient(ellipse 60% 90% at 50% 40%, var(--damask-light) 0%, transparent 75%),
      linear-gradient(180deg, var(--damask-mid) 0%, var(--damask-dark) 100%);
  }
  .header-rule {
    position: absolute;
    left: 0;
    top: 195px;
    width: 848px;
    height: 36px;
    background: var(--band);
  }
  .brand-badge {
    position: absolute;
    left: 332px;
    top: 147px;
    width: 175px;
    height: 134px;
  }
  .brand-badge svg {
    position: absolute;
    inset: 0;
  }
  .brand-mark {
    position: absolute;
    left: 50%;
    top: 28px;
    width: 36px;
    height: 36px;
    margin-left: -18px;
    border: 2px solid var(--ink);
    border-radius: 50%;
    box-sizing: border-box;
  }
  .brand-name,
  .brand-sub {
    position: absolute;
    left: 0;
    right: 0;
    margin: 0;
    text-align: center;
    font-family: "Playfair Display", serif;
    font-weight: 700;
    line-height: 1;
    color: var(--ink);
  }
  .brand-name {
    top: 80px;
    font-size: 22px;
    letter-spacing: 1.5px;
  }
  .brand-sub {
    top: 108px;
    font-size: 7px;
    letter-spacing: 3.5px;
  }
</style>
</head>
<body>
  <main class="letterhead">
    <div class="paper-pattern" role="img" aria-label="Faint cream monogram damask pattern across the sheet"></div>
    <div class="header-damask" role="img" aria-label="Black and ivory damask pattern with crowns and crest medallions"></div>
    <div class="header-rule"></div>

    <div class="brand-badge">
      <svg viewBox="0 0 174 132" width="175" height="134" aria-hidden="true">
        <path d="M15,3 H159 Q159,14 171,14 V112 Q159,112 159,122 H98 L87,129 L76,122 H15 Q15,112 3,112 V14 Q15,14 15,3 Z"
              fill="var(--ink)"/>
        <path d="M19,8 H155 Q156,18 166,19 V107 Q156,108 155,117 H96 L87,122 L78,117 H19 Q18,108 8,107 V19 Q18,18 19,8 Z"
              fill="var(--cream)"/>
        <path d="M22,11 H152 Q153,20 163,21 V105 Q153,106 152,114 H95 L87,118 L79,114 H22 Q21,106 11,105 V21 Q21,20 22,11 Z"
              fill="none" stroke="var(--ink)" stroke-width="1"/>
      </svg>
      <span class="brand-mark"></span>
      <p class="brand-name">VELBRIN</p>
      <p class="brand-sub">GLOBAL</p>
    </div>
  </main>
</body>
</html>
```